Sunwell Prime Cleaning Service , Inc wants to make the buck so make it happen = )

I need a postcard design for my cleaning company. I have full ownership and 15+ years experience. At this time we take care of residential clients as well as commercial clients. Mainly offices. I do plan to expand my business in the commercial aspect. My experience is that we compete with franchise companies and my company deliveries a higher quality of work.
I already have a logo designed which I would like to use. Basically we do high quality, detail oriented work not just the first time to get the client but years and years ahead.

Target Market(s)

Commercial Offices

Industry/Entity Type

Residential

Font styles to use
Serif
Sans Serif

Colors
9bcb3c
ec1f27
33a6d7
3075b4
f78f20

Requirements
Must have
• focusing on quality, reliability, wants to stand of the crowd
Nice to have
• anything that makes the sale
Should not have
• too much general cleaning company adds

```html
<!DOCTYPE html>
<html lang="en">
<head>
<meta charset="utf-8">
<title>Sunwell Prime Cleaning Service, Inc — Flyer and Postcard</title>
<link href="https://fonts.googleapis.com/css2?family=Roboto+Condensed:wght@400;500;700&family=Open+Sans:wght@400;600&family=Patrick+Hand&display=swap" rel="stylesheet">
<style>
  :root {
    --green: #9bcb3c;
    --orange: #f78f20;
    --blue: #33a6d7;
    --navy: #3075b4;
    --deep: #1d5c9c;
    --grey: #8a8a8a;
    --ink: #222;
    --stage: #ecebe8;
  }
  * { box-sizing: border-box; margin: 0; padding: 0; }
  html, body { width: 1200px; height: 692px; overflow: hidden; background: var(--stage); }
  body { position: relative; font-family: "Open Sans", sans-serif; }

  .flyer, .postcard {
    position: absolute; background: #fff; overflow: hidden;
    box-shadow: 0 6px 18px rgba(0,0,0,.25);
  }
  .flyer { left: 52px; top: 49px; width: 463px; height: 598px;
    background: linear-gradient(#d9edfa 0, #fff 90px, #fff 320px, #f2f2f2 100%); }
  .postcard { left: 562px; top: 184px; width: 601px; height: 463px;
    background: linear-gradient(#d4ebf9 0, #eef6fc 60px, #fff 110px, #f4f4f4 100%); }

  .brand { position: absolute; display: flex; align-items: center; gap: 8px; z-index: 2; }
  .brand-dot { border-radius: 50%; background: var(--navy); flex: none; }
  .brand-name { font-family: "Roboto Condensed", sans-serif; font-weight: 700; color: var(--navy); line-height: 1.05; }

  .flyer .brand { left: 18px; top: 22px; }
  .flyer .brand-dot { width: 34px; height: 34px; }
  .flyer .brand-name { font-size: 22px; }

  .serving { position: absolute; right: 28px; top: 14px; z-index: 2; text-align: center;
    font-family: "Patrick Hand", cursive; font-size: 17px; line-height: 19px; color: var(--ink); }
  .serving .area { color: var(--orange); }

  .photo { position: absolute; left: 0; top: 78px; width: 463px; height: 228px;
    background: linear-gradient(100deg, #9fb2c4 0%, #c9d8e6 45%, #dfe7ee 70%, #b8c6d3 100%); }
  .waves { position: absolute; left: 0; top: 70px; }

  .badge { position: absolute; left: 20px; top: 180px; width: 66px; height: 66px; border-radius: 50%; z-index: 2;
    background: #f4fbe8; border: 4px solid var(--green); color: var(--deep);
    font-family: "Patrick Hand", cursive; text-align: center; font-size: 11px; line-height: 11px; padding-top: 16px; }
  .badge b { font-size: 15px; font-weight: 400; }

  .tagline { position: absolute; left: 44px; top: 232px; z-index: 2; font-family: "Patrick Hand", cursive;
    font-size: 21px; line-height: 30px; color: var(--orange); text-shadow: 1px 1px 0 #3a2a10; }

  .services-title { position: absolute; left: 0; right: 0; top: 342px; text-align: center;
    font-family: "Roboto Condensed", sans-serif; font-weight: 700; font-size: 19px; color: var(--navy); }

  .column { position: absolute; top: 366px; }
  .column h3 { font-family: "Roboto Condensed", sans-serif; font-weight: 400; font-size: 18px; color: var(--orange); margin-bottom: 3px; }
  .column ul { list-style: none; }
  .column li { display: flex; align-items: center; gap: 8px; font-size: 11.5px; color: var(--grey); height: 19.3px; white-space: nowrap; }
  .column .bullet { width: 12px; height: 12px; flex: none; }
  .col-commercial { left: 29px; }
  .col-residential { left: 268px; }

  .promise { position: absolute; right: 26px; top: 468px; text-align: center;
    font-family: "Patrick Hand", cursive; font-size: 14px; line-height: 16px; color: var(--green); }

  .mission { position: absolute; left: 0; right: 0; top: 508px; text-align: center; }
  .mission h4 { font-family: "Patrick Hand", cursive; font-weight: 400; font-size: 16px; color: var(--orange); }
  .mission p { font-size: 9px; color: var(--grey); }

  .callbar { position: absolute; left: 0; bottom: 0; height: 42px; display: flex; align-items: center;
    background: linear-gradient(90deg, var(--deep), var(--blue)); color: #fff; white-space: nowrap; }
  .flyer .callbar { width: 463px; padding-left: 25px; gap: 18px; }
  .callbar .lead { font-size: 15px; flex: none; }
  .callbar .phone { display: flex; align-items: center; gap: 8px; font-weight: 600; font-size: 23px; flex: none; }
  .callbar .phone svg { width: 26px; height: 26px; }

  .postcard .brand { left: 27px; top: 34px; }
  .postcard .brand-dot { width: 44px; height: 44px; }
  .postcard .brand-name { font-size: 30px; }

  .stamp { position: absolute; left: 486px; top: 32px; width: 95px; height: 64px; border: 1.5px solid #aaa; }
  .address-lines { position: absolute; left: 391px; top: 151px; width: 190px; }
  .address-lines span { display: block; height: 27.7px; border-top: 1.5px solid #b5b5b5; }

  .pc-title { position: absolute; left: 32px; top: 135px; font-family: "Roboto Condensed", sans-serif;
    font-weight: 500; font-size: 14px; color: var(--navy); }
  .checklist { position: absolute; left: 34px; top: 157px; list-style: none; }
  .checklist li { display: flex; align-items: center; gap: 6px; height: 20.8px; white-space: nowrap;
    font-family: "Roboto Condensed", sans-serif; font-weight: 500; font-size: 13.5px; color: var(--green); }
  .checklist svg { width: 13px; height: 13px; flex: none; }

  .contact { position: absolute; left: 27px; top: 326px; font-family: "Patrick Hand", cursive; color: var(--orange); }
  .contact h4 { font-weight: 400; font-size: 16px; margin-bottom: 4px; }
  .contact p { font-size: 15.5px; line-height: 19.5px; }
  .contact .tel { font-size: 17px; letter-spacing: .5px; }

  .postcard .callbar { width: 357px; padding-left: 20px; gap: 10px; }
  .postcard .callbar .lead { font-size: 11.5px; letter-spacing: -.2px; }
  .postcard .callbar .phone { font-size: 18px; gap: 7px; }
  .postcard .callbar .phone svg { width: 21px; height: 21px; }
</style>
</head>
<body>

<svg width="0" height="0" style="position:absolute">
  <defs>
    <symbol id="icon-phone" viewBox="0 0 26 26">
      <circle cx="13" cy="13" r="11.5" fill="none" stroke="#fff" stroke-width="2"/>
      <path d="M9 7.5c.6-.5 1.4-.4 1.8.2l1.2 1.9c.3.5.2 1.1-.2 1.5l-.8.7c.6 1.4 1.8 2.6 3.2 3.2l.7-.8c.4-.4 1-.5 1.5-.2l1.9 1.2c.6.4.7 1.2.2 1.8l-.9 1c-.6.6-1.5.8-2.3.5-3.3-1.3-5.900-3.9-7.200-7.200-.3-.8-.1-1.7.5-2.300z" fill="#fff"/>
    </symbol>
    <symbol id="icon-arrow" viewBox="0 0 12 12">
      <circle cx="6" cy="6" r="6" fill="#9bcb3c"/>
      <path d="M5 3.5 7.5 6 5 8.5" fill="none" stroke="#fff" stroke-width="1.6"/>
    </symbol>
    <symbol id="icon-tick" viewBox="0 0 13 13">
      <rect x="1" y="2" width="10" height="10" rx="1.5" fill="none" stroke="#3075b4" stroke-width="1.4"/>
      <path d="M3.5 6.5 6 9l6-7.5" fill="none" stroke="#3075b4" stroke-width="1.6"/>
    </symbol>
  </defs>
</svg>

<article class="flyer">
  <div class="photo" role="img" aria-label="Photo of a smiling cleaner in a blue apron holding a mop in a bright open-plan office"></div>
  <svg class="waves" width="463" height="245" viewBox="0 0 463 245" aria-hidden="true">
    <path d="M0 0H463V8C360 -2 260 20 180 34 110 46 50 42 0 30Z" fill="#eaf5fc"/>
    <path d="M0 30C60 44 120 42 200 28 280 14 380 4 463 10V18C380 12 290 22 210 36 130 50 60 52 0 40Z" fill="#3075b4"/>
    <path d="M190 30C280 10 380 0 463 4V10C380 6 290 16 190 30Z" fill="#9bcb3c"/>
    <path d="M0 190C90 228 220 240 463 210V245H0Z" fill="#fff"/>
    <path d="M0 196C100 230 240 238 463 216V226C250 246 100 238 0 208Z" fill="#9bcb3c"/>
    <path d="M0 206C100 238 250 246 463 224V232C250 252 100 246 0 214Z" fill="#3075b4"/>
  </svg>

  <div class="brand">
    <span class="brand-dot"></span>
    <span class="brand-name">Sunwell Prime<br>Cleaning Service, Inc.</span>
  </div>
  <div class="serving">Proudly serving<br><span class="area">Tampa Bay area</span><br>since 1999.</div>

  <div class="badge"><b>15+</b> years<br>experience</div>
  <p class="tagline">Professional quality<br>for a professional space.</p>

  <h2 class="services-title">COMMERCIAL AND RESIDENTIAL CLEANING SERVICES</h2>

  <section class="column col-commercial">
    <h3>Commercial Cleaning</h3>
    <ul>
      <li><svg class="bullet"><use href="#icon-arrow"/></svg>Apartment Buildings</li>
      <li><svg class="bullet"><use href="#icon-arrow"/></svg>Professional Offices</li>
      <li><svg class="bullet"><use href="#icon-arrow"/></svg>Property Management Companies</li>
      <li><svg class="bullet"><use href="#icon-arrow"/></svg>Realtors</li>
      <li><svg class="bullet"><use href="#icon-arrow"/></svg>Financial Institutions / Banks</li>
      <li><svg class="bullet"><use href="#icon-arrow"/></svg>Hair Salons / Nail Salons / Spas</li>
    </ul>
  </section>
  <section class="column col-residential">
    <h3>Residential Cleaning</h3>
    <ul>
      <li><svg class="bullet"><use href="#icon-arrow"/></svg>Move In / Out cleaning</li>
      <li><svg class="bullet"><use href="#icon-arrow"/></svg>Spring Cleaning</li>
      <li><svg class="bullet"><use href="#icon-arrow"/></svg>Cleaning All living areas</li>
    </ul>
  </section>

  <p class="promise">High quality, detail oriented work.<br>Not just the first time - every time!</p>

  <div class="mission">
    <h4>Our mission</h4>
    <p>is to make everyday life easier for families and companies by taking care of their home or office.</p>
  </div>

  <div class="callbar">
    <span class="lead">Call today for your FREE QUOTE</span>
    <span class="phone"><svg><use href="#icon-phone"/></svg>555 014 2380</span>
  </div>
</article>

<article class="postcard">
  <div class="brand">
    <span class="brand-dot"></span>
    <span class="brand-name">Sunwell Prime<br>Cleaning Service, Inc.</span>
  </div>
  <div class="stamp"></div>
  <div class="address-lines"><span></span><span></span><span></span><span></span></div>

  <h2 class="pc-title">RESIDENTIAL AND COMMERCIAL CLEANING SERVICES</h2>
  <ul class="checklist">
    <li><svg><use href="#icon-tick"/></svg>Family Owned and Operated</li>
    <li><svg><use href="#icon-tick"/></svg>Insured</li>
    <li><svg><use href="#icon-tick"/></svg>Background checked employees</li>
    <li><svg><use href="#icon-tick"/></svg>Fully flexible customized service plans</li>
    <li><svg><use href="#icon-tick"/></svg>Available to respond to immediate needs</li>
    <li><svg><use href="#icon-tick"/></svg>Ongoing efforts to assure quality and customer satisfaction</li>
    <li><svg><use href="#icon-tick"/></svg>100% satisfaction guaranteed</li>
  </ul>

  <div class="contact">
    <h4>Please Contact Us:</h4>
    <p class="tel">p: 555.014.2380</p>
    <p>e: hello@sunwellprimeclean.com</p>
    <p>www.sunwellprimeclean.com</p>
  </div>

  <div class="callbar">
    <span class="lead">Call today for your FREE QUOTE</span>
    <span class="phone"><svg><use href="#icon-phone"/></svg>555 014 2380</span>
  </div>
</article>

</body>
</html>
```